Business Card Design Project for Architecture and Interior Design company

We need a business card design and logo for an architecture and design firm located in Santiago de Chile. It´s a small company, and the name is "Ostrevo" ("Ostr" from my surname Ostrini, and "arq" for arquitectura or architecture. But it would also be nice that the logo comunicates de Word game "Bella" as beautiful in italian, and "arq" as architecture".
The idea is to give a delicate, elegant and sofisticated, yet fresh image. Would prefer grey black and white colors, but wouldn´t mind to use another additional color.
I allready have a web page www.ostrevo-studio.example, but would like to improve the logo design.
Please contact if any further information is requiered.
Reason: Need a more arquitectural and desing spirit in the cards. Few of them give that idea.

```html
<!DOCTYPE html>
<html lang="es">
<head>
<meta charset="utf-8">
<title>Ostrevo — Business Card Options</title>
<link rel="stylesheet" href="https://fonts.googleapis.com/css2?family=Open+Sans:wght@300;400&family=EB+Garamond:wght@400;500&family=Arimo:wght@700&display=swap">
<style>
  :root {
    --paper: #ffffff;
    --card-black: #1f1b1a;
    --card-grey: #5f5c5c;
    --band-grey: #9b9b9b;
    --band-black: #1a1717;
    --ink-white: #ffffff;
    --ink-soft: #d9d9d9;
    --label-ink: #1a1a1a;
  }
  html, body {
    margin: 0;
    width: 1200px;
    height: 735px;
    overflow: hidden;
    background: var(--paper);
  }
  .sheet {
    position: relative;
    width: 1200px;
    height: 735px;
  }
  .option {
    position: absolute;
    width: 588px;
  }
  .option--top-left { left: 0; top: 0; }
  .option--top-right { left: 612px; top: 0; }
  .option--bottom-left { left: 0; top: 383px; }
  .option--bottom-right { left: 612px; top: 383px; }

  .option__label {
    height: 28px;
    margin: 0;
    text-align: center;
    font: 700 14px/14px "Arimo", Arial, sans-serif;
    color: var(--label-ink);
    padding-top: 0;
    position: relative;
    top: -2px;
  }
  .option--bottom-left .option__label,
  .option--bottom-right .option__label { top: 6px; }

  .card {
    position: relative;
    height: 307px;
    overflow: hidden;
  }
  .card--black { background: var(--card-black); }
  .card--grey { background: var(--card-grey); }

  .card__name {
    position: absolute;
    left: 34px;
    top: 57px;
    margin: 0;
    font-size: 25px;
    font-weight: 400;
    line-height: 32px;
  }
  .card__contact {
    position: absolute;
    left: 34px;
    top: 232px;
    margin: 0;
    font-size: 14px;
    line-height: 18.5px;
    font-style: normal;
  }
  .card__wordmark {
    position: absolute;
    left: 360px;
    top: 232px;
    width: 200px;
    margin: 0;
    font-size: 46px;
    line-height: 50px;
    text-align: center;
  }

  .card--sans { font-family: "Open Sans", Arial, sans-serif; color: var(--ink-white); }
  .card--sans .card__wordmark { font-weight: 300; }

  .card--serif { font-family: "EB Garamond", Georgia, serif; color: var(--ink-soft); }
  .card--serif .card__name { font-weight: 500; font-size: 27px; }
  .card--serif .card__contact { font-size: 14.5px; }
  .card--serif .card__wordmark { font-weight: 500; letter-spacing: 1px; }

  .band {
    height: 15px;
    margin-top: 3px;
  }
  .band--grey { background: var(--band-grey); }
  .band--black { background: var(--band-black); }
</style>
</head>
<body>
<main class="sheet">

  <section class="option option--top-left">
    <h2 class="option__label">OPTION 1</h2>
    <div class="card card--black card--sans">
      <p class="card__name">Mira Ostrini</p>
      <address class="card__contact">Contacto: info@ostrevo-studio.example<br>Fono: +56 9 5550 1234<br>www.ostrevo-studio.example</address>
      <p class="card__wordmark">Ostrevo</p>
    </div>
    <div class="band band--grey"></div>
  </section>

  <section class="option option--top-right">
    <h2 class="option__label">OPTION 3</h2>
    <div class="card card--grey card--sans">
      <p class="card__name">Mira Ostrini</p>
      <address class="card__contact">Contacto: info@ostrevo-studio.example<br>Fono: +56 9 5550 1234<br>www.ostrevo-studio.example</address>
      <p class="card__wordmark">Ostrevo</p>
    </div>
    <div class="band band--black"></div>
  </section>

  <section class="option option--bottom-left">
    <h2 class="option__label">OPTION 2</h2>
    <div class="card card--black card--serif">
      <p class="card__name">Mira Ostrini</p>
      <address class="card__contact">Contacto: info@ostrevo-studio.example<br>Fono: +56 9 5550 1234<br>www.ostrevo-studio.example</address>
      <p class="card__wordmark">OSTREVO</p>
    </div>
    <div class="band band--grey"></div>
  </section>

  <section class="option option--bottom-right">
    <h2 class="option__label">OPTION 2</h2>
    <div class="card card--grey card--serif">
      <p class="card__name">Mira Ostrini</p>
      <address class="card__contact">Contacto: info@ostrevo-studio.example<br>Fono: +56 9 5550 1234<br>www.ostrevo-studio.example</address>
      <p class="card__wordmark">OSTREVO</p>
    </div>
    <div class="band band--grey"></div>
  </section>

</main>
</body>
</html>
```